Facebook Header Design Project.

I'm supplying white and colored logos. The Facebook page already exists. URL = https://www.pagebook.example/lumocrest.design The design should not be based on what's already there. Consider mobile implications of the design. This Design will form the designs of other social media headers. LumoCrest is a web design | digital marketing company.

Target Market(s)

People interested in web design | digital marketing services.

Industry/Entity Type

LumoCrest is a web design | digital marketing company. That should be clear in the design.

Colors
0054AA
0677BA
7BADD7
CADEEF
E8F1F8

Requirements
Must have
• Logo. Use Facebook header image dimension.
Nice to have
• Use a color scheme like the logo and feel free to add a color or two from the other side of the color whee.

```html
<!DOCTYPE html>
<html lang="en">
<head>
<meta charset="utf-8">
<title>LumoCrest – Web Design &amp; Digital Marketing Header</title>
<link rel="stylesheet" href="https://fonts.googleapis.com/css2?family=Quicksand:wght@500&display=swap">
<style>
  :root {
    --night: #0a1020;
    --glow: #0f1d52;
    --slate-deep: #1c2a3a;
    --slate: #2a3b4d;
    --slate-light: #3a4f62;
    --frame-cream: #f4eed6;
    --accent-blue: #1a9cf0;
    --text-blue: #8cc6f2;
    --white: #ffffff;
  }
  * { margin: 0; padding: 0; box-sizing: border-box; }
  html, body {
    width: 1200px;
    height: 615px;
    overflow: hidden;
    background: var(--night);
  }
  .header-canvas {
    position: relative;
    width: 1200px;
    height: 615px;
    overflow: hidden;
    background: radial-gradient(ellipse 480px 300px at 600px 330px, var(--glow) 0%, var(--night) 100%);
    font-family: "Quicksand", sans-serif;
    font-weight: 500;
  }
  .backdrop {
    position: absolute;
    inset: 0;
    width: 1200px;
    height: 615px;
  }
  .brand-mark {
    position: absolute;
    left: 139px;
    top: 92px;
    display: flex;
    align-items: center;
    gap: 10px;
    color: var(--white);
    font-size: 34px;
    line-height: 1;
  }
  .brand-mark .brand-dot {
    width: 12px;
    height: 12px;
    border-radius: 50%;
    background: var(--white);
  }
  .service-label {
    position: absolute;
    left: 0;
    width: 1200px;
    text-align: center;
    top: 214px;
    color: var(--text-blue);
    font-size: 36px;
    letter-spacing: 3px;
    line-height: 1;
  }
  .company-name {
    position: absolute;
    left: 0;
    width: 1200px;
    text-align: center;
    top: 272px;
    color: var(--white);
    font-size: 118px;
    line-height: 1;
  }
  .tagline {
    position: absolute;
    left: 0;
    width: 1200px;
    text-align: center;
    top: 397px;
    color: var(--text-blue);
    font-size: 32px;
    letter-spacing: 0.5px;
    line-height: 1;
  }
</style>
</head>
<body>
<main class="header-canvas">
  <svg class="backdrop" viewBox="0 0 820 420" preserveAspectRatio="none" aria-hidden="true">
    <!-- large curved bands -->
    <path class="band-top" d="M380 0 C 470 55, 640 95, 820 100 L820 0 Z" fill="var(--slate-deep)"/>
    <path class="band-top-highlight" d="M640 0 C 680 60, 760 95, 820 95 L820 0 Z" fill="var(--slate-light)"/>
    <path class="band-bottom-left" d="M0 255 C 140 245, 300 300, 470 420 L0 420 Z" fill="var(--slate-deep)"/>
    <path class="band-bottom-left-inner" d="M0 330 C 120 330, 230 370, 300 420 L0 420 Z" fill="var(--slate)"/>
    <path class="band-bottom-right" d="M820 265 C 760 300, 745 380, 770 420 L820 420 Z" fill="var(--slate)"/>

    <!-- decorative areas kept as flat tones -->
    <rect role="img" aria-label="Diagonal stripe texture" x="0" y="160" width="120" height="170" fill="var(--slate-deep)" opacity="0.45"/>
    <rect role="img" aria-label="Dot grid texture" x="95" y="95" width="90" height="45" fill="var(--slate)" opacity="0.25"/>
    <rect role="img" aria-label="Dot grid texture" x="610" y="150" width="110" height="90" fill="var(--slate)" opacity="0.2"/>

    <!-- cream line frames -->
    <g fill="none" stroke="var(--frame-cream)" stroke-width="2">
      <polyline class="frame-upper" points="545,152 720,152 720,162"/>
      <polyline class="frame-main-left" points="305,170 108,170 108,300"/>
      <polyline class="frame-main-right" points="498,170 723,170 723,308 435,308"/>
      <polyline class="frame-outer-left" points="240,188 93,188 93,210"/>
      <polyline class="frame-lower" points="130,295 130,335 340,335"/>
      <line class="frame-lower-right" x1="706" y1="200" x2="706" y2="265"/>
    </g>

    <!-- blue accent dashes -->
    <g stroke="var(--accent-blue)" stroke-width="3" stroke-linecap="butt">
      <line x1="518" y1="152" x2="537" y2="152"/>
      <line x1="250" y1="188" x2="276" y2="188"/>
      <line x1="93" y1="226" x2="93" y2="246"/>
      <line x1="130" y1="266" x2="130" y2="290"/>
      <line x1="706" y1="268" x2="706" y2="292"/>
      <line x1="350" y1="338" x2="415" y2="338"/>
    </g>
  </svg>

  <div class="brand-mark">
    <span class="brand-dot"></span>
    <span class="brand-name">LumoCrest</span>
  </div>

  <p class="service-label">WEB DESIGN</p>
  <h1 class="company-name">LumoCrest</h1>
  <p class="tagline">digital marketing services</p>
</main>
</body>
</html>
```